We need an attractive business card design that is modern and inviting. We like the blue and yellow (or gold) colors that are displayed with the logo. The business should communicate trust, experience, and integrity.

Target Market(s)

Residential and Commercial

Industry/Entity Type

Business

Contact Information for Business Card

Recessed Lighting
LED Retro Fit
Sign Repair
Alarms and Cameras
Mobile Home Services
24hr service calls

Font styles to use
Serif
Sans Serif

Colors
3176b5
0455a3
fece3e
fbee3e

Requirements
Must have
• Brondle Electric
• Owner: Marcus Tivane
• Licensed and Insured
• TECL #58917
Nice to have
• Exquisite Detail!!
• Over 20 years of experience
Should not have
• Nothing boring or traditional!!!

```html
<!DOCTYPE html>
<html lang="en">
<head>
<meta charset="utf-8">
<title>Brondle Electric – Business Card</title>
<link rel="stylesheet" href="https://fonts.googleapis.com/css2?family=Open+Sans:wght@400;700&display=swap">
<style>
  :root {
    --ink-blue: #0b3ea8;
    --brand-blue: #0455a3;
    --gold-deep: #d9b70a;
    --gold-mid: #ebcf1e;
    --gold-light: #fbee3e;
    --card-white: #ffffff;
    --backdrop: #ebe8e3;
  }
  html, body {
    margin: 0;
    width: 1200px;
    height: 1000px;
    overflow: hidden;
    background: var(--backdrop);
    font-family: "Open Sans", sans-serif;
    color: var(--ink-blue);
  }
  .canvas { position: relative; width: 1200px; height: 1000px; }
  .card {
    position: absolute;
    background: var(--card-white);
    box-shadow: 0 3px 10px rgba(0,0,0,0.25);
    overflow: hidden;
  }
  .card-front { left: 48px; top: 82px; width: 660px; height: 376px; }
  .card-back  { left: 483px; top: 543px; width: 659px; height: 377px; }
  .facet-art { position: absolute; inset: 0; width: 100%; height: 100%; }
  .text { position: absolute; margin: 0; line-height: 1; white-space: nowrap; }

  .brand-lockup {
    position: absolute; left: 362px; top: 84px;
    display: flex; align-items: center; gap: 8px;
  }
  .brand-dot {
    width: 24px; height: 24px; border-radius: 50%;
    border: 3px solid var(--brand-blue); box-sizing: border-box;
  }
  .brand-name {
    font-size: 22px; font-weight: 700; letter-spacing: 0.5px;
    color: var(--brand-blue);
  }
  .owner-name { left: 79px; top: 192px; font-size: 26px; font-weight: 700; }
  .owner-rule {
    position: absolute; left: 79px; top: 229px; width: 240px; height: 2px;
    background: var(--ink-blue);
  }
  .owner-title { left: 79px; top: 235px; font-size: 21px; font-weight: 400; }
  .company-block {
    position: absolute; right: 61px; top: 266px; text-align: right;
  }
  .company-block p { margin: 0; line-height: 21px; font-size: 17px; }
  .company-block .company-name { font-size: 20px; font-weight: 700; line-height: 26px; }

  .service-rule {
    position: absolute; left: 116px; top: 83px; width: 2px; height: 225px;
    background: var(--ink-blue);
  }
  .experience-heading { left: 144px; top: 103px; font-size: 22px; font-weight: 700; }
  .service-list {
    position: absolute; left: 144px; top: 139px; margin: 0; padding: 0;
    list-style: none; font-size: 18px; line-height: 20px;
  }
</style>
</head>
<body>
<div class="canvas">

  <section class="card card-front">
    <svg class="facet-art" viewBox="0 0 660 376" role="img" aria-label="Low-poly gold facet pattern in the top-left corner">
      <defs>
        <linearGradient id="goldFront" x1="0" y1="0" x2="1" y2="1">
          <stop offset="0" stop-color="var(--gold-light)"/>
          <stop offset="0.5" stop-color="var(--gold-mid)"/>
          <stop offset="1" stop-color="var(--gold-deep)"/>
        </linearGradient>
      </defs>
      <polygon points="0,0 357,0 265,83 117,96 60,150 0,298" fill="url(#goldFront)"/>
    </svg>

    <div class="brand-lockup">
      <span class="brand-dot"></span>
      <span class="brand-name">BRONDLE ELECTRIC</span>
    </div>

    <h1 class="text owner-name">Marcus Tivane</h1>
    <div class="owner-rule"></div>
    <p class="text owner-title">Owner</p>

    <div class="company-block">
      <p class="company-name">Brondle Electric</p>
      <p>Licensed and Insured</p>
      <p>TECL #58917</p>
    </div>
  </section>

  <section class="card card-back">
    <svg class="facet-art" viewBox="0 0 659 377" role="img" aria-label="Low-poly gold facet patterns in the top-left and right corners">
      <defs>
        <linearGradient id="goldBack" x1="0" y1="0" x2="1" y2="1">
          <stop offset="0" stop-color="var(--gold-light)"/>
          <stop offset="0.5" stop-color="var(--gold-mid)"/>
          <stop offset="1" stop-color="var(--gold-deep)"/>
        </linearGradient>
      </defs>
      <polygon points="0,0 128,0 57,62 0,157" fill="url(#goldBack)"/>
      <polygon points="659,5 547,122 529,202 535,282 447,377 659,377" fill="url(#goldBack)"/>
    </svg>

    <div class="service-rule"></div>
    <h2 class="text experience-heading">Over 20 years of experience</h2>
    <ul class="service-list">
      <li>- Recidential and Comercial</li>
      <li>- Recessed Lighting</li>
      <li>- LED Retro Fit</li>
      <li>- Sign Repair</li>
      <li>- Alarms and Camera</li>
      <li>- Mobile Home Service</li>
      <li>- 24hr service calls</li>
    </ul>
  </section>

</div>
</body>
</html>
```